Guaranteed Job - Sleek Sexy Business Card UV Spot

Im looking for a sleek and sexy business card, that resembles elite or VIP status status.
our business is corinvale.example
you can view our products on there, but our main audience for handing out our cards will be for people in the hospitality industry, so it will need to impress high management and CEO of hotels and restaurants, bars, clubs etc...
the card features will have UV spot on both sides, 400gsm stock. standard size.
Artwork should be 86 x 54mm + 2mm bleed = 90 x 58mm
it should have a nice "unique" uv spot pattern that highlights the card, not a repeated pattern, theres no originality there, and it will be disregarded.
The written material will be:
Corin Vale Hospitality College (logo)
Tobin Marsh
Director
Phone: 1300 615 737
Mobile: 0455 817 296
Email: info@corinvale.example
website: www.corinvale.example
I'm looking for originality here, i don't want just a simple stock card, want something that has a wow factor for people.
You will find the logo attached. you may invert the white to black words to suit the background as you please.
thank you and good luck
As a side note, ive received a lot of proposals, im too busy to give feedback to each and every one, so if i havent provided feedback for your design within 24 hours, then consider it not acceptable, and you could resubmit another design.
So far i have not seen any design that stood out for me, they all seem pretty generic. there nothing thats unique, i would figure for the amount that im offering, that people would put some more effort and creativity into the design.
so far over 200 designs submitted, and nothing i have seen looks very original, everything looks like a different variation of the same stuff, i said it very clearly i wanted something unique, the only thing that has come close to it so far is this one
Reason: Ive received alot of design concepts and i have reviewed everyone, but i havent had time to give feedback to every single one, only the ones that have interested me, if i havent responded, its because i havent found it good enough.
so far only a few design have been on par with what ive been looking for, an attractive eye popping design.
heres a few of them,
http://files.pixelbazaar.example/design_img/51736/62418/62418_2840915_51736_image.jpg
http://files.pixelbazaar.example/design_img/51736/68254/68254_2841377_51736_image.jpg
theyre, both unique and original, and eye catching, the only thing theyre missing is the sexyness.
if you still think you have some creativity left in your minds, then throw it on here.
Reason: Sorry guys for the delay, I was in a serious accident and out of commission for the past few months, I'm just slowly recovering now, please bare with me as i try to attend to this project, it may take me awhile as I have other projects that are on standby, I'm not 100% at the moment, so im extending the deadline for 2 weeks right now. Thanks for your patience.
Hospitality

```html
<!DOCTYPE html>
<html lang="en">
<head>
<meta charset="utf-8">
<title>Corin Vale Hospitality College – Business Card</title>
<link rel="stylesheet" href="https://fonts.googleapis.com/css2?family=Arimo:wght@400;700&display=swap">
<style>
  :root {
    --page: #ffffff;
    --card-dark: #264655;
    --card-mid: #35535f;
    --card-light: #3d5a66;
    --accent: #4a9fd8;
    --ink: #ffffff;
    --ink-soft: #d9e2e6;
    --spot-dark: rgba(10, 22, 28, 0.55);
    --spot-fade: rgba(10, 22, 28, 0);
  }
  * { box-sizing: border-box; margin: 0; padding: 0; }
  html, body {
    width: 1200px;
    height: 900px;
    overflow: hidden;
    background: var(--page);
    font-family: "Arimo", Arial, sans-serif;
  }
  .canvas {
    position: relative;
    width: 1200px;
    height: 900px;
  }
  .card {
    position: absolute;
    width: 560px;
    height: 361px;
    background: linear-gradient(105deg, var(--card-dark) 0%, var(--card-mid) 45%, var(--card-light) 100%);
    overflow: hidden;
  }
  .card--front { left: 60px; top: 70px; }
  .card--back { left: 580px; top: 470px; }

  .uv-spot {
    position: absolute;
    top: -10px;
    right: 20px;
    width: 210px;
    height: 210px;
    background: radial-gradient(circle at 50% 45%, var(--spot-dark) 0%, rgba(10,22,28,0.25) 45%, var(--spot-fade) 72%);
  }
  .card--back .uv-spot {
    top: 70px;
    right: -10px;
    width: 190px;
    height: 190px;
  }

  .brand {
    position: absolute;
    display: flex;
    align-items: center;
    gap: 14px;
  }
  .brand__square {
    background: var(--accent);
    flex: none;
  }
  .brand__name {
    color: var(--ink);
    font-weight: 700;
    text-transform: uppercase;
    line-height: 1.05;
  }
  .card--front .brand { left: 50px; bottom: 58px; }
  .card--front .brand__square { width: 64px; height: 64px; }
  .card--front .brand__name { font-size: 25px; }

  .card--back .brand { left: 26px; top: 28px; gap: 9px; }
  .card--back .brand__square { width: 30px; height: 30px; }
  .card--back .brand__name { font-size: 12px; }

  .holder {
    position: absolute;
    left: 44px;
    top: 196px;
    color: var(--ink);
  }
  .holder__name {
    font-size: 22px;
    font-weight: 400;
    letter-spacing: 0.5px;
  }
  .holder__role {
    font-size: 13px;
    margin-top: 3px;
    color: var(--ink-soft);
  }
  .contact {
    list-style: none;
    margin-top: 20px;
    font-size: 14px;
    line-height: 1.35;
  }
  .contact__item { display: flex; gap: 10px; }
  .contact__label { color: var(--accent); width: 10px; }
  .contact__value { color: var(--ink); }
</style>
</head>
<body>
<main class="canvas">

  <section class="card card--front" aria-label="Business card front">
    <div class="uv-spot" role="img" aria-label="UV spot pattern of interlocking rounded squares"></div>
    <div class="brand">
      <span class="brand__square"></span>
      <span class="brand__name">Corin Vale<br>Hospitality College</span>
    </div>
  </section>

  <section class="card card--back" aria-label="Business card back">
    <div class="uv-spot" role="img" aria-label="UV spot pattern of interlocking rounded squares"></div>
    <div class="brand">
      <span class="brand__square"></span>
      <span class="brand__name">Corin Vale<br>Hospitality College</span>
    </div>
    <div class="holder">
      <p class="holder__name">TOBIN MARSH</p>
      <p class="holder__role">Director</p>
      <ul class="contact">
        <li class="contact__item"><span class="contact__label">P</span><span class="contact__value">1300 615 737</span></li>
        <li class="contact__item"><span class="contact__label">M</span><span class="contact__value">0455 817 296</span></li>
        <li class="contact__item"><span class="contact__label">E</span><span class="contact__value">info@corinvale.example</span></li>
        <li class="contact__item"><span class="contact__label">W</span><span class="contact__value">www.corinvale.example</span></li>
      </ul>
    </div>
  </section>

</main>
</body>
</html>
```